Flyer-Design für Vermittlung von Büromaschinen
Zielgruppe
Wir vertreiben Büromaschinen hauptsächlich hochwertige Kopierautomaten für Büros, Steuerberater, Rechtsanwälte usw.
Besonderen Augenmerk auf gebrauchte, generalüberholte Maschinen zur Miete an den Kunden, damit die Rohstoffe möglichst lange genutzt werden um die Umwelt zu schonen. zum Beispiel:
Willkommen in der Wegwerfgesellschaft.
Früher oder später wird alles weggeworfen. In der Konsumgesellschaft wandern aber auch gebrauchsfertige und neuwertige Produkte auf den Müll. Dieses hat fatale Konsequenzen: Klimawandel, Artensterben, Wassermangel- schon heute für viele existenzbedrohend. So wie wir wirtschaften, kann es nicht weitergehen! Wir müssen Rohstoffe möglichst lange nutzen, um dadurch die Umwelt zu schonen, denn wenn wir so weitermachen wie bisher werden 2050 mehr Plastik in unseren Ozeanen schwimmen als Fische. Helfen Sie uns beim Aufbau einer erfolgreichen Nutzungsform, bei der funktionstüchtige Kopierautomaten weiterhin eingesetzt werden sodass sichergestellt wird das Rohstoffe möglichst lange genutzt werden, um dadurch die Umwelt zu schonen. Bitte beachten Sie unser beigefügtes Angebot damit die Nachhaltigkeit gewinnt.
Wir kaufen gebrauchte Kopierautomaten von Leasinggesellschaften und bereiten diese in unserer Werkstatt auf. Diese dann neuwertigen, funktionstüchtigen Maschinen sollen dann vermietet werden.
Aufgabenstellung
Wir benötigen einen Flyer und ein entsprechendes Anschreiben.
Bilder und Texte können von der Website entnommen werden:
https://www.lummerich-buerotechnik.de/
Bei Anfrage kann ich Ihnen auch gerne die Bilder zur Verfügung stellen.
Bezüglich der Texte, würde ich mich auch über Vorschläge von Ihrer Seite freuen.

```html
<!DOCTYPE html>
<html lang="de">
<head>
<meta charset="utf-8">
<title>Lummerich – Vermietung neuwertiger Gebrauchtgeräte</title>
<link href="https://fonts.googleapis.com/css2?family=Roboto:ital,wght@1,900&family=Roboto+Condensed:wght@300;400&family=Source+Sans+3:wght@300;400;600&display=swap" rel="stylesheet">
<style>
:root{
  --navy:#2b2c6e;
  --red:#e2231a;
  --arrow:#3e56a6;
  --text:#555555;
  --page:#dcdcdd;
  --white:#ffffff;
  --table:#3b5ab0;
}
*{box-sizing:border-box;margin:0;padding:0}
html,body{width:1176px;height:1200px;overflow:hidden;background:var(--page)}
body{position:relative;font-family:"Source Sans 3",sans-serif;color:var(--text)}
.panel{position:absolute;background:var(--white);overflow:hidden;width:578px;height:579px}
.panel--cover{left:10px;top:9px}
.panel--title{left:590px;top:9px;width:576px}
.panel--cycle{left:10px;top:612px}
.panel--offer{left:590px;top:612px;width:576px}
.abs{position:absolute}
.visual{position:absolute}

.band{position:absolute;left:0;bottom:0;width:100%;height:43px;background:var(--navy);color:var(--white);
  display:flex;align-items:center;justify-content:center;overflow:hidden;
  font-family:"Roboto Condensed",sans-serif;font-weight:300;font-size:21px;letter-spacing:1.4px;white-space:nowrap}

.brand-name{font-family:"Source Sans 3",sans-serif;font-weight:600;color:var(--navy);font-size:50px;line-height:1;letter-spacing:.5px}
.brand-tag{font-family:"Source Sans 3",sans-serif;font-weight:400;color:var(--red);font-size:20px;line-height:1}
.address{left:70px;top:414px;font-size:12.6px;line-height:15px;letter-spacing:.9px;font-weight:400;color:var(--text);font-style:normal}
.address p+p{margin-top:4px}

.claim{position:absolute;background:var(--navy);color:var(--white);font-family:"Roboto",sans-serif;font-weight:900;font-style:italic;
  font-size:21.5px;line-height:24.5px;letter-spacing:.5px;white-space:nowrap}

.heading{position:absolute;font-family:"Roboto Condensed",sans-serif;font-weight:400;color:var(--navy);font-size:22.5px;line-height:1;white-space:nowrap}

.copy{position:absolute;font-size:12.2px;line-height:16.6px;letter-spacing:.35px;font-weight:300;color:var(--text)}
.copy .line{display:block;white-space:nowrap;text-align:justify;text-align-last:justify}
.copy .line--end{text-align-last:left}

.step{position:absolute;font-size:12.4px;line-height:16.5px;letter-spacing:1.2px;text-align:center;color:var(--text)}
.step-no{position:absolute;font-family:"Roboto Condensed",sans-serif;font-weight:300;font-size:30px;color:var(--text);line-height:1}
.motto{position:absolute;left:186px;top:354px;width:180px;text-align:center;font-family:"Roboto",sans-serif;font-weight:900;font-style:italic;
  color:var(--red);font-size:15.4px;line-height:18px;letter-spacing:1.4px}
.cycle-arrow{position:absolute;width:78px;height:78px}
.cycle-arrow path{fill:var(--arrow)}

.price-table{position:absolute;left:74px;top:168px;transform:rotate(-9deg);transform-origin:left top;
  font-family:"Roboto Condensed",sans-serif;color:var(--table);font-size:13px;border-collapse:collapse}
.price-table td{padding:2px 6px;white-space:nowrap}
.price-table td.num{text-align:center;width:46px}
.price-table tr:nth-child(odd) td{background:rgba(180,200,235,.55)}
.price-note{position:absolute;left:250px;top:270px;transform:rotate(-9deg);font-family:"Roboto Condensed",sans-serif;font-size:10px;color:#6e7a99;white-space:nowrap}

.promo{position:absolute;left:340px;top:150px;width:236px;height:170px}
.promo-text{font-family:"Roboto",sans-serif;font-weight:900;font-style:italic;fill:var(--white)}

.includes{position:absolute;left:231px;top:389px;width:345px;height:71px;background:var(--navy);color:var(--white);
  font-family:"Roboto",sans-serif;font-weight:900;font-style:italic;font-size:13.2px;line-height:16.5px;padding:10px 10px 0 13px;white-space:nowrap}
</style>
</head>
<body>

<section class="panel panel--cover">
  <div class="visual" role="img" aria-label="Foto: gewölbtes Papierblatt mit aufgedrucktem Erdball" style="left:0;top:0;width:520px;height:470px;background:radial-gradient(ellipse 190px 110px at 260px 130px,#3f6a8a 0%,#5e7f55 45%,#c9b488 70%,rgba(255,255,255,0) 72%),linear-gradient(160deg,#ffffff 10%,#ececec 60%,#ffffff 100%)"></div>
  <div class="abs brand-name" style="left:59px;top:328px">Lummerich</div>
  <div class="abs brand-tag" style="left:83px;top:370px">Büro- und KopierSysteme</div>
  <address class="abs address">
    <p>Lummerich<br>Büro- und KopierSysteme GmbH<br>Ampèreweg 8, 50999 Falkenrath</p>
    <p>Tel: 02234 – 48 26 90</p>
    <p>info@lummerich-buerotechnik.de<br>www.lummerich-buerotechnik.de</p>
  </address>
  <div class="band">+++ VERMIETUNG NEUWERTIGER GEBRAUCHTGERÄTE +++</div>
</section>

<section class="panel panel--title">
  <div class="visual" role="img" aria-label="Foto: Kopiergerät gibt ein Blatt mit aufgedrucktem Erdball aus" style="left:0;top:0;width:302px;height:536px;background:linear-gradient(180deg,#4a515c 0%,#e8e9ec 12%,#cfd2d6 20%,#3e434c 30%,#5a616b 60%,#3a3f47 100%)"></div>
  <div class="visual" role="img" aria-label="Blatt mit Erdball" style="left:0;top:220px;width:320px;height:190px;background:radial-gradient(ellipse 95px 62px at 200px 100px,#3f6a8a 0%,#6a8a5a 50%,#c9b488 75%,rgba(240,240,240,0) 78%),#f1f1f1;clip-path:polygon(0 45%,70% 0,100% 80%,45% 100%)"></div>
  <div class="visual" style="left:302px;top:0;width:274px;height:536px;background:linear-gradient(90deg,#ffffff 60%,#d9d9db 100%)"></div>
  <div class="claim" style="left:311px;top:65px;width:265px;height:87px;padding:8px 0 0 16px">HELFEN SIE MIT,<br>NACHHALTIG<br>ZU WIRTSCHAFTEN ...</div>
  <div class="claim" style="left:323px;top:224px;width:253px;height:106px;padding:3px 0 0 8px;clip-path:polygon(0 0,100% 0,100% 100%,8% 100%,8% 88%,0 82%)">... DENN<br><span style="padding-left:23px">UNSER PLANET</span><br><span style="padding-left:23px">LÄSST SICH</span><br><span style="padding-left:23px">NICHT KOPIEREN!</span></div>
  <div class="abs brand-name" style="left:311px;top:454px">Lummerich</div>
  <div class="abs brand-tag" style="left:335px;top:498px">Büro- und KopierSysteme</div>
  <div class="band">+++ VERMIETUNG NEUWERTIGER GEBRAUCHTGERÄTE +++</div>
</section>

<section class="panel panel--cycle">
  <h2 class="heading" style="left:45px;top:24px">FRÜHER ODER SPÄTER WIRD ALLES WEGGEWORFEN</h2>
  <p class="copy" style="left:46px;top:52px;width:220px">
    <span class="line">In unserer Konsumgesellschaft wan-</span>
    <span class="line">dern aber auch funktionstüchtige</span>
    <span class="line">und neuwertige Produkte auf dem</span>
    <span class="line">Müll. Dieses hat fatale Konsequenzen:</span>
  </p>
  <p class="copy" style="left:295px;top:52px;width:222px">
    <span class="line">Klimawandel, Artensterben, Wasser-</span>
    <span class="line">mangel. So wie wir wirtschaften, kann</span>
    <span class="line">es nicht weitergehen! Nutzen Sie vor-</span>
    <span class="line line--end">handene Rohstoffe.</span>
  </p>

  <div class="visual" role="img" aria-label="Foto: Multifunktions-Kopiersystem mit Finisher" style="left:172px;top:176px;width:155px;height:154px;background:linear-gradient(90deg,#3d3f44 0%,#55585e 55%,#e9eaec 72%,#cfd1d4 100%);border-radius:4px"></div>

  <svg class="cycle-arrow" style="left:107px;top:148px" viewBox="0 0 100 100" aria-hidden="true"><path d="M22 95 C12 55 32 26 64 20 L60 4 L97 30 L66 58 L64 40 C44 43 33 62 36 95 Z"/></svg>
  <svg class="cycle-arrow" style="left:408px;top:208px;transform:rotate(90deg)" viewBox="0 0 100 100" aria-hidden="true"><path d="M22 95 C12 55 32 26 64 20 L60 4 L97 30 L66 58 L64 40 C44 43 33 62 36 95 Z"/></svg>
  <svg class="cycle-arrow" style="left:360px;top:350px;transform:rotate(180deg)" viewBox="0 0 100 100" aria-hidden="true"><path d="M22 95 C12 55 32 26 64 20 L60 4 L97 30 L66 58 L64 40 C44 43 33 62 36 95 Z"/></svg>
  <svg class="cycle-arrow" style="left:107px;top:312px;transform:rotate(270deg)" viewBox="0 0 100 100" aria-hidden="true"><path d="M22 95 C12 55 32 26 64 20 L60 4 L97 30 L66 58 L64 40 C44 43 33 62 36 95 Z"/></svg>

  <span class="step-no" style="left:342px;top:160px">2</span>
  <p class="step" style="left:362px;top:160px;width:100px">Aufbereitung<br>in unserer<br>Werkstatt</p>
  <span class="step-no" style="left:55px;top:270px">1</span>
  <p class="step" style="left:70px;top:250px;width:100px">Ankauf<br>gebrauchter<br>Leasing-Geräte</p>
  <p class="step" style="left:370px;top:309px;width:130px">Vermietung dieser<br>neuwertigen<br>Geräte</p>
  <span class="step-no" style="left:496px;top:313px">3</span>

  <p class="motto">GEMEINSAM<br>WIRTSCHAFTEN<br>WIR NACHHALTIG</p>

  <h2 class="heading" style="left:45px;top:453px">PROFITIEREN SIE UND UNSERE UMWELT ...</h2>
  <p class="copy" style="left:46px;top:480px;width:220px">
    <span class="line">... von unserem Mietservice für</span>
    <span class="line line--end">generalüberhole Multifunktionsgeräte.</span>
  </p>
  <p class="copy" style="left:293px;top:480px;width:224px">
    <span class="line">Mieten statt kaufen! Sie sparen nachhal-</span>
    <span class="line">tig und unsere Umwelt wird geschont!</span>
  </p>
  <div class="band">+++ VERMIETUNG NEUWERTIGER GEBRAUCHTGERÄTE +++</div>
</section>

<section class="panel panel--offer">
  <h2 class="heading" style="left:51px;top:24px">WIR STEHEN IHNEN FLEXIBEL ZUR SEITE ...</h2>
  <p class="copy" style="left:53px;top:52px;width:220px">
    <span class="line line--end">... und reagieren schnell und einfach auf</span>
    <span class="line line--end">Ihren kurz- oder langfristigen Bedarf an</span>
    <span class="line line--end">Kopiersystemen.</span>
  </p>
  <p class="copy" style="left:302px;top:52px;width:222px">
    <span class="line">Durch ein einfaches Preismodell und eine</span>
    <span class="line">unkomplizierte Abwicklung können Sie</span>
    <span class="line">Ihr Gerät schnell und bequem einsetzen.</span>
  </p>

  <div class="visual" role="img" aria-label="Foto: Laserdrucker gibt ein gewölbtes Blatt mit Preistabelle und Erdball aus" style="left:0;top:105px;width:576px;height:430px;background:radial-gradient(ellipse 105px 90px at 262px 238px,#3f6a8a 0%,#6a8a5a 55%,#c9b488 78%,rgba(245,245,240,0) 80%),linear-gradient(180deg,#ffffff 0%,#f4f4ef 45%,#d2d3d5 62%,#b9bbbe 100%)"></div>

  <table class="price-table">
    <tr><td>Mietpreis pro Monat</td><td class="num">59,- €</td><td class="num">65,- €</td><td class="num">69,- €</td></tr>
    <tr><td>incl. Farbseiten / Monat</td><td class="num">50</td><td class="num">100</td><td class="num">200</td></tr>
    <tr><td>incl. s/w Seiten / Monat</td><td class="num">500</td><td class="num">1000</td><td class="num">2000</td></tr>
    <tr><td>Preis je Folgeseite Farbe</td><td class="num">0,10 €</td><td class="num">0,09 €</td><td class="num">0,08 €</td></tr>
    <tr><td>Preis je Folgeseite s/w</td><td class="num">0,02 €</td><td class="num">0,018 €</td><td class="num">0,013 €</td></tr>
  </table>
  <span class="price-note">Angebot solange Vorrat reicht</span>

  <svg class="promo" viewBox="340 150 236 170" aria-label="Schon ab 59,- € pro Monat">
    <polygon points="362,222 404,196 418,276 372,264" fill="#e2231a"/>
    <polygon points="408,198 547,188 538,256 440,278 446,300 426,282" fill="#e2231a"/>
    <path d="M552 164 L562 152 M558 176 L570 172 M366 286 L356 300 M378 292 L374 306 M390 294 L394 308" stroke="#e2231a" stroke-width="4" stroke-linecap="round"/>
    <g class="promo-text" transform="rotate(-6 480 235)">
      <text x="420" y="221" font-size="14">SCHON AB</text>
      <text x="446" y="252" font-size="30">59,- €</text>
      <text x="490" y="262" font-size="8">PRO MONAT</text>
    </g>
  </svg>

  <div class="includes">Im Preis sind alle anfallenden Kosten enthalten:<br>Miete, Freikopien, Wartung und Service<br>sowie Verbrauchsmaterien.</div>
  <div class="band">+++ VERMIETUNG NEUWERTIGER GEBRAUCHTGERÄTE +++</div>
</section>

</body>
</html>
```